Product Label Design

Need a product design for our Epsom salt product, needs to have a luxurious simple feel to it. The picture attached is our brand and wordage on it, the bag we think should be a stand up bag that should be offwhite/creme color. The other picture are products that we like. We updated the packaging to be a Kraft tube box, please see the attached photo for dimensions.

```html
<!DOCTYPE html>
<html lang="en">
<head>
<meta charset="utf-8">
<title>Nova Bath Salts — Label Proposal</title>
<link rel="stylesheet" href="https://fonts.googleapis.com/css2?family=IBM+Plex+Mono:wght@400;500;700&family=Archivo:wght@700&display=swap">
<style>
  :root {
    --backdrop: #e1e5d9;
    --label-paper: #f3f3ec;
    --ink: #111111;
    --mint: #8dcea2;
  }
  * { margin: 0; padding: 0; box-sizing: border-box; }
  html, body {
    width: 1200px;
    height: 1200px;
    overflow: hidden;
    background: var(--backdrop);
  }
  .canvas {
    position: relative;
    width: 1200px;
    height: 1200px;
    font-family: "IBM Plex Mono", monospace;
    color: var(--ink);
  }
  .edge-banner {
    position: absolute;
    top: 586px;
    width: 1200px;
    height: 28px;
    display: flex;
    justify-content: center;
    align-items: center;
    font-weight: 700;
    font-size: 22px;
    letter-spacing: 0.02em;
    white-space: nowrap;
  }
  .edge-banner--left { left: -564px; transform: rotate(-90deg); }
  .edge-banner--right { left: 564px; transform: rotate(90deg); }
  .label {
    position: absolute;
    left: 360px;
    top: 220px;
    width: 480px;
    height: 684px;
  }
  .label svg { display: block; width: 100%; height: 100%; }
  .label-note {
    position: absolute;
    left: 0;
    top: 940px;
    width: 1200px;
    text-align: center;
    font-size: 20px;
    font-weight: 500;
    letter-spacing: 0.03em;
  }
</style>
</head>
<body>
<main class="canvas">
  <div class="edge-banner edge-banner--left">NOVA LABEL PROPOSAL • NOVA LABEL PROPOSAL • NOVA LABEL PROPOSAL • NOVA LABEL PROPOSAL</div>
  <div class="edge-banner edge-banner--right">NOVA LABEL PROPOSAL • NOVA LABEL PROPOSAL • NOVA LABEL PROPOSAL • NOVA LABEL PROPOSAL</div>

  <section class="label" aria-label="Bath salts label">
    <svg viewBox="0 0 658 938" xmlns="http://www.w3.org/2000/svg">
      <defs>
        <clipPath id="label-bounds"><rect width="658" height="938"/></clipPath>
      </defs>
      <rect class="label-paper" width="658" height="938" fill="var(--label-paper)"/>

      <g font-family="IBM Plex Mono, monospace" fill="var(--ink)">
        <text class="tag-premium" x="619" y="36" font-size="15" text-anchor="end">PREMIUM</text>
        <text class="tag-bath-salts" transform="translate(623 22) rotate(90)" font-size="15">BATH SALTS</text>

        <text class="brand-name" x="329" y="272" font-size="130" font-weight="700" text-anchor="middle">Nova</text>

        <text class="ingredient-main" x="329" y="639" font-size="17" font-weight="700" text-anchor="middle">US Sourced Pure Epsom Salt</text>
        <text class="ingredient-sub" x="329" y="661" font-size="17" text-anchor="middle">(Magnesium Sulfate)</text>

        <g class="ingredient-list" font-size="17">
          <path d="M171 698 l3 4 l6 -8" fill="none" stroke="var(--ink)" stroke-width="1.8"/>
          <text x="184" y="705">Abies sibirica</text>
          <path d="M373 698 l3 4 l6 -8" fill="none" stroke="var(--ink)" stroke-width="1.8"/>
          <text x="386" y="705">Fir Balsam</text>
        </g>

        <text class="tag-bath-salts" transform="translate(34 910) rotate(-90)" font-size="15">BATH SALTS</text>
        <text class="tag-premium" transform="translate(38 898) rotate(180)" font-size="15" text-anchor="end">PREMIUM</text>

        <text class="net-weight" x="624" y="901" font-size="13" font-weight="500" text-anchor="end">NET WT. 3 LB (1,360 G)</text>
      </g>

      <g clip-path="url(#label-bounds)">
        <text class="scent-name" x="-14" y="551" font-family="Archivo, sans-serif" font-weight="700" font-size="208"
              textLength="684" lengthAdjust="spacingAndGlyphs"
              fill="none" stroke="var(--mint)" stroke-width="3">REVIVE</text>
      </g>
    </svg>
  </section>

  <p class="label-note">(TRANSPARENT LABEL)</p>
</main>
</body>
</html>
```